Website Design for a "Talent Recruitment Agency"

We are looking for a website design for the website of our "Talent Recruitment Agency"; which is called "Crestway Hub".
Our recruitment website "Crestway Hub" will be focusing on: "Crestway Hub: Linking People & Firms in Switzerland"; which means our target audience is two-folded:
(i) TALENT - that is currently residing in- or outside of Switzerland, and is open for and interested in the "Swiss Job Market".
(ii) COMPANIES - that are looking for talent for specific job vacancies in Switzerland.
With our "Crestway Hub" approach we inted to focus on Membership & Partnership:
(a)"Membership"(TALENT)
and
(b)"Partnership"(COMPANIES)
Some of the competitor sites we like are:
• www.plimora42.dk
• www.qelvo.ch
• www.brandolix.ch/en
A sitemap example of our website is attached.
Also attached is a "Crestway Hub" logo in .eps format and one in .jpeg format.
We very much look forward to receive your creative ideas.
Best regards,
Crestway Hub
Crestway Hub: Linking People & Firms in Switzerland.
Website: crestwayhub.ch - Twitter: CrestwayHubCH
Target Market(s)
(i) TALENT (with around 0-10 years of working experience), currently residing in- or outside of Switzerland, but eligible to work in Switzerland.
(ii) COMPANIES (national or international) that are based in Switzerland.
Industry/Entity Type
Recruitment

```html
<!DOCTYPE html>
<html lang="en">
<head>
<meta charset="utf-8">
<title>Crestway Hub – Linking People & Firms in Switzerland</title>
<link rel="stylesheet" href="https://fonts.googleapis.com/css2?family=Yanone+Kaffeesatz:wght@400;500&family=Open+Sans:wght@400;600&display=swap">
<style>
:root{
  --orange:#f47322;
  --orange-dark:#e4621a;
  --blue:#0a8fd0;
  --blue-deep:#0b5d9c;
  --ink:#222;
  --nav-ink:#5a2a0e;
  --grey-bg:#efefef;
  --grey-line:#d8d8d8;
  --white:#fff;
}
*{box-sizing:border-box;margin:0;padding:0}
html,body{width:777px;height:1200px;overflow:hidden;background:var(--white)}
body{font-family:"Open Sans",sans-serif;color:var(--ink);position:relative}
.page{width:777px;height:1200px;position:relative;overflow:hidden}

.site-header{height:103px;background:var(--grey-bg);display:flex;align-items:center;justify-content:center;gap:12px}
.brand-mark{width:62px;height:62px;border-radius:50%;background:var(--blue)}
.brand-name{font-weight:600;font-size:32px;color:var(--orange)}

.main-nav{height:35px;background:linear-gradient(#ff9a4e,var(--orange) 45%,var(--orange-dark));border-top:2px solid #fbc9a4;position:relative}
.main-nav ul{list-style:none;display:flex;align-items:center;justify-content:space-between;position:absolute;left:62px;top:0;width:513px;height:33px}
.main-nav li{font-family:"Yanone Kaffeesatz",sans-serif;font-size:14px;letter-spacing:.4px;color:var(--nav-ink);text-transform:uppercase;white-space:nowrap}
.lang-select{position:absolute;left:646px;top:8px;width:95px;height:17px;background:var(--white);font-size:8px;color:#444;display:flex;align-items:center;justify-content:space-between;padding:0 6px 0 11px;white-space:nowrap}

.hero{height:291px;background:radial-gradient(ellipse at 40% 20%,#28b6ea,#0a72b8 55%,var(--blue-deep))}

.intro{height:151px;text-align:center;padding-top:54px;background:linear-gradient(var(--white),#f7f7f7)}
.intro h1{font-family:"Yanone Kaffeesatz",sans-serif;font-weight:500;font-size:25px;line-height:28px;color:var(--orange);text-transform:uppercase;letter-spacing:.5px}
.intro p{font-size:12.4px;line-height:16px;width:700px;margin:4px auto 0}

.audiences{height:341px;background:linear-gradient(#e6e6e6,#f8f8f8 60%,var(--white));display:flex;justify-content:space-between;padding:24px 63px 0 68px}
.audience{width:286px}
.audience h2{font-family:"Yanone Kaffeesatz",sans-serif;font-weight:500;font-size:26px;line-height:30px;color:var(--blue);text-align:center}
.audience .rule{height:12px;margin:8px -18px 0;background:radial-gradient(ellipse at 50% 0,rgba(0,0,0,.45),rgba(0,0,0,0) 70%)}
.audience p{font-size:9.5px;line-height:14.2px;text-align:justify;padding:14px 6px 0;height:150px}
.btn{display:block;height:28px;margin-bottom:3px;color:var(--white);font-size:12.5px;text-align:center;line-height:28px;text-transform:uppercase;white-space:nowrap}
.btn.orange{background:var(--orange)}
.btn.blue{background:var(--blue)}

.lower{height:215px;background:linear-gradient(#e9e9e9,#f4f4f4);display:flex;padding:10px 0 0 67px}
.lower h3{font-family:"Yanone Kaffeesatz",sans-serif;font-weight:500;font-size:18px;line-height:22px;color:#111;text-transform:uppercase;letter-spacing:.4px}
.lower .rule{height:8px;margin-top:5px;background:radial-gradient(ellipse at 30% 0,rgba(0,0,0,.3),rgba(0,0,0,0) 70%)}
.jobs{width:301px}
.job{display:flex;justify-content:space-between;align-items:center;gap:6px;padding:6px 0 5px;border-bottom:1px solid var(--grey-line);height:43px}
.job-title{font-size:10.4px;line-height:14px;color:#111;white-space:nowrap;letter-spacing:-.1px}
.job-meta{font-size:8.8px;line-height:12px;color:var(--blue);white-space:nowrap}
.apply{flex-shrink:0;white-space:nowrap;background:var(--blue);color:var(--white);font-size:9.8px;padding:3px 6px;border:1px solid #0670a8}
.more{text-align:right;font-size:9.5px;color:var(--orange);margin-top:9px}
.more span{border-bottom:1px solid var(--orange)}
.contact{width:315px;margin-left:56px}
.offices{display:flex;margin-top:6px}
.office{width:176px;font-size:9px;line-height:13px;white-space:nowrap}
.office + .office{border-left:1px solid var(--grey-line);padding-left:23px;width:139px}
.office h4{font-weight:400;font-size:11.5px;color:var(--blue);margin-bottom:8px}
.office .gap{margin-top:10px}
.office a{color:var(--orange);text-decoration:none}

.site-footer{height:64px;background:var(--blue);display:flex;justify-content:space-between;align-items:center;padding:0 67px 0 68px}
.site-footer p{color:var(--white);font-size:9px;line-height:13px}
.social{display:flex;gap:10px}
.social span{width:22px;height:22px;border-radius:50%;background:var(--white)}
</style>
</head>
<body>
<div class="page">
  <header class="site-header">
    <span class="brand-mark"></span>
    <span class="brand-name">Crestway Hub</span>
  </header>

  <nav class="main-nav">
    <ul>
      <li>Home</li><li>|</li>
      <li>About</li><li>|</li>
      <li>Talent</li><li>|</li>
      <li>Companies</li><li>|</li>
      <li>Jobs</li><li>|</li>
      <li>Events</li><li>|</li>
      <li>Contact</li>
    </ul>
    <div class="lang-select">Select Language
      <svg width="8" height="6" viewBox="0 0 8 6"><path d="M1 1l3 3 3-3" stroke="#222" stroke-width="1.8" fill="none"/></svg>
    </div>
  </nav>

  <div class="hero" role="img" aria-label="Silhouettes of professionals standing in front of a glowing blue map of Switzerland"></div>

  <section class="intro">
    <h1>Crestway Hub: Linking People &amp; Firms in Switzerland</h1>
    <p>Lorem ipsum dolor sit amet, consectetur adipiscing elit. Quisque at vulputate sem. Sed cursus at nibh ac hendrerit. Proin lectus dui, blandit ac ultricies a, ultrices at lacus.</p>
  </section>

  <section class="audiences">
    <div class="audience">
      <h2>TALENT</h2>
      <div class="rule"></div>
      <p>Maecenas urna eros, semper et metus sed, iaculis porttitor lacus. Aenean in velit sit amet odio lacinia tempor et eu neque. Etiam id ipsum ut urna ultricies porta. Ut congue scelerisque ligula, ut auctor velit. Vestibulum ante ipsum primis in faucibus orci luctus et ultrices posuere cubilia Curae; Aenean aliquam, erat at congue condimentum, enim est convallis nulla, quis sollicitudin libero dolor a felis. Integer sit amet cursus nulla. Sed pharetra commodo viverra.</p>
      <span class="btn orange">Membership &amp; Benefits</span>
      <span class="btn blue">Get Registered</span>
      <span class="btn orange">CV Uploads</span>
    </div>
    <div class="audience">
      <h2>COMPANIES</h2>
      <div class="rule"></div>
      <p>Maecenas urna eros, semper et metus sed, iaculis porttitor lacus. Aenean in velit sit amet odio lacinia tempor et eu neque. Etiam id ipsum ut urna ultricies porta. Ut congue scelerisque ligula, ut auctor velit. Vestibulum ante ipsum primis in faucibus orci luctus et ultrices posuere cubilia Curae; Aenean aliquam, erat at congue condimentum, enim est convallis nulla, quis sollicitudin libero dolor a felis. Integer sit amet cursus nulla. Sed pharetra commodo viverra.</p>
      <span class="btn orange">Login &nbsp;|&nbsp; Registration</span>
      <span class="btn blue">Partnerships &amp; Benefits</span>
      <span class="btn orange">Talent Request</span>
    </div>
  </section>

  <section class="lower">
    <div class="jobs">
      <h3>Current Jobs / Vacancies</h3>
      <div class="rule"></div>
      <div class="job"><div><div class="job-title">HR Operations Management Consultant</div><div class="job-meta">Zurich, Consulting</div></div><span class="apply">Apply Now</span></div>
      <div class="job"><div><div class="job-title">Consultant Process Engineering &amp; Operations</div><div class="job-meta">Geneva, Telecommunication</div></div><span class="apply">Apply Now</span></div>
      <div class="job"><div><div class="job-title">Investment Analysis</div><div class="job-meta">Zurich, Financial Services</div></div><span class="apply">Apply Now</span></div>
      <div class="more"><span>Browse More Jobs</span></div>
    </div>
    <div class="contact">
      <h3>Contact Us</h3>
      <div class="rule"></div>
      <div class="offices">
        <div class="office">
          <h4>Office 1</h4>
          Linden Court 11<br>8001 Zurich
          <div class="gap">Phone: <a>+41 44 555 0187</a><br>Email Id: <a>info@crestwayhub.ch</a><br>website: <a>www.crestwayhub.ch</a></div>
        </div>
        <div class="office">
          <h4>Office 2</h4>
          Birchway House 75<br>6300 Zug
          <div class="gap">Phone: <a>+41 44 555 0187</a><br>Email Id: <a>info@crestwayhub.ch</a><br>website: <a>www.crestwayhub.ch</a></div>
        </div>
      </div>
    </div>
  </section>

  <footer class="site-footer">
    <p>Home &nbsp;|&nbsp; About &nbsp;|&nbsp; Talent &nbsp;|&nbsp; Companies &nbsp;|&nbsp; Jobs &nbsp;|&nbsp; Events &nbsp;|&nbsp; Contact<br>© 2014, All Rights Reserved</p>
    <div class="social"><span></span><span></span><span></span><span></span></div>
  </footer>
</div>
</body>
</html>
```